Business Card Design

We need a design that will also transfer to car decals
We need a design that will speak to the average person needing home and office remodeling
The design should be fresh, exciting, easy to read in a glance and unique
We would like a die-cut tool belt
Bright colors and evenly spaced information

Target Market(s)

Home and business owners
Middle and Upper Income property owners
Families and people with fixer upper homes

Industry/Entity Type

Business

Contact Information for Business Card

Looking for the best Bay Area Handyman? Here I am!
RKW Handyman Services does it all at prices regular people can afford.
Electrical, Plumbing, Carpentry, Remodeling, Fencing, Picture and window placement, Hauling ... and anything else you can imagine!
510-374-2196
Serving the Entire Bay Area
Free Estimates! Call us Today to turn your dreams into reality!

Font styles to use
Serif

Requirements
Must have
• Speaks to the average person
stands out among similar industry cards
Nice to have
• fun, comical, you want to hold on to this card
Should not have
• bland colors
look too crowded

```html
<!DOCTYPE html>
<html lang="en">
<head>
<meta charset="utf-8">
<title>RKW Handyman Services – Business Card</title>
<link rel="stylesheet" href="https://fonts.googleapis.com/css2?family=Cinzel:wght@500;700;800&display=swap">
<style>
  :root {
    --page-bg: #d6d6d6;
    --card-bg: #1b1b1b;
    --card-bg-light: #262626;
    --accent: #ea4a1c;
    --ink: #ffffff;
    --belt-dark: #3c3c3c;
    --belt-grey: #8e9297;
  }
  * { box-sizing: border-box; margin: 0; padding: 0; }
  html, body {
    width: 1200px;
    height: 900px;
    overflow: hidden;
    background: var(--page-bg);
    font-family: "Cinzel", "Times New Roman", serif;
  }
  .sheet {
    width: 1200px;
    height: 900px;
    display: flex;
    flex-direction: column;
    align-items: center;
    justify-content: center;
    gap: 36px;
  }
  .card {
    position: relative;
    width: 720px;
    height: 410px;
    border-radius: 16px;
    background: radial-gradient(ellipse at 50% 40%, var(--card-bg-light), var(--card-bg) 75%);
    color: var(--ink);
    text-align: center;
    box-shadow: 0 6px 18px rgba(0,0,0,0.25);
    overflow: hidden;
  }

  /* Front */
  .card-front { padding-top: 26px; }
  .front-question {
    font-size: 22px;
    font-weight: 700;
    letter-spacing: 1px;
  }
  .tool-belt {
    width: 460px;
    height: 190px;
    margin: 18px auto 0;
    border-radius: 18px;
    background:
      radial-gradient(ellipse at 50% 65%, rgba(234,74,28,0.55), rgba(234,74,28,0) 70%),
      linear-gradient(180deg, var(--belt-grey) 0%, var(--belt-dark) 100%);
  }
  .front-intro {
    margin-top: 24px;
    font-size: 26px;
    font-weight: 700;
    color: var(--accent);
    letter-spacing: 0.5px;
  }
  .front-tagline {
    margin-top: 4px;
    font-size: 19px;
    font-weight: 700;
    letter-spacing: 0.5px;
  }
  .highlight { color: var(--accent); }

  /* Back */
  .card-back { padding-top: 34px; }
  .back-name {
    font-size: 30px;
    font-weight: 700;
    color: var(--accent);
    letter-spacing: 0.5px;
  }
  .service-list {
    margin-top: 22px;
    font-size: 17px;
    font-weight: 700;
    line-height: 1.45;
    letter-spacing: 0.3px;
  }
  .call-to-action {
    margin-top: 40px;
    font-size: 19px;
    font-weight: 700;
    color: var(--accent);
    letter-spacing: 0.3px;
  }
  .phone {
    margin-top: 6px;
    font-size: 38px;
    font-weight: 700;
    letter-spacing: 1px;
  }
  .service-area {
    margin-top: 36px;
    font-size: 21px;
    font-weight: 700;
    letter-spacing: 0.5px;
  }
</style>
</head>
<body>
<main class="sheet">
  <section class="card card-front">
    <p class="front-question">Looking for the Best Bay Area Handyman?</p>
    <div class="tool-belt" role="img" aria-label="Illustration of an orange and grey tool belt holding a screwdriver, pliers, saw, wrench, tape measure and hammer"></div>
    <p class="front-intro">Here I am! RKW Handyman Services</p>
    <p class="front-tagline">does it <span class="highlight">all</span> at prices regular people can afford.</p>
  </section>

  <section class="card card-back">
    <h1 class="back-name">RKW Handyman Services</h1>
    <p class="service-list">
      Electrical, Plumbing, Carpentry, Remodeling,<br>
      Fencing, Picture and Window Placement, Hauling<br>
      And Anything Else You Can Imagine!
    </p>
    <p class="call-to-action">Call us Today to turn your Dreams into Reality!</p>
    <p class="phone">510-374-2196</p>
    <p class="service-area">Serving The Entire Bay Area. Free Estimates!</p>
  </section>
</main>
</body>
</html>
```